Whole body Cryotherapy Tri fold Brochure

I am looking to do a tri fold brochure for a whole body cryotherapy business called Fernvale Cryotherapy.I do not have imagery but i would like to try to utilize images to support the benefits of Whole body cryotherapy. I will provide the content needed for the different sides. We would like to see blues and whatever would flow with the design. Also the machine that i will be using is called a PELOM and i would like to add that to the side flap of the brochure. I would really like this to be a modern unique twist since this type of treatment is fairly new to the United states.

Target Market(s)

women, men, children, athletes, health , modern medicine , alternative medicine

Industry/Entity Type

Alternative Medicine

Font styles to use
Sans Serif

Requirements
Must have
• Modern design with bold features, big colorful pictures.
Nice to have
• Font styles can be changed as well. Br

```html
<!DOCTYPE html>
<html lang="en">
<head>
<meta charset="utf-8">
<title>Fernvale Cryotherapy – Tri-fold Brochure</title>
<link href="https://fonts.googleapis.com/css2?family=Open+Sans:wght@400;600;700;800&display=swap" rel="stylesheet">
<style>
:root{
  --navy:#0b2f6b;
  --blue:#1565c0;
  --sky:#2b8fd6;
  --ice:#d9ecf8;
  --text:#2f3a45;
  --muted:#6b7885;
  --white:#ffffff;
  --page:#e9eef2;
}
*{margin:0;padding:0;box-sizing:border-box}
html,body{width:793px;height:1200px;overflow:hidden;background:var(--page);font-family:'Open Sans',Arial,sans-serif;color:var(--text)}
.spread{position:absolute;left:0;width:793px;height:588px;display:grid;grid-template-columns:repeat(3,1fr);background:var(--white);box-shadow:0 1px 4px rgba(0,0,0,.15)}
.spread.outside{top:0}
.spread.inside{top:612px}
.panel{position:relative;overflow:hidden;padding:18px 18px;font-size:7.4px;line-height:1.5}
.panel + .panel{border-left:1px solid #e3e8ec}
h2{color:var(--blue);font-weight:700;font-size:17px;line-height:1.15;margin-bottom:12px}
p{margin-bottom:8px}
.stats{display:flex;gap:20px;margin:10px 0 14px;text-align:center;font-weight:700;color:var(--blue);font-size:7.5px}
.stats svg{display:block;margin:0 auto 4px}
.seen-head{margin:-18px -18px 16px;background:var(--blue);color:var(--white);text-align:center;padding:14px 10px;font-weight:700}
.seen-head .small{font-size:11px;font-weight:600}
.seen-head .big{font-size:14px;line-height:1.2}
.badges{display:grid;grid-template-columns:repeat(4,1fr);gap:10px 12px;margin:6px 6px 26px}
.badge{height:34px;border-radius:50%;background:#dde4ea;width:34px;margin:auto}
.badge.sq{border-radius:4px;width:44px}
.contact{text-align:center;font-weight:700;color:var(--navy);font-size:8px;line-height:1.6;margin-top:10px}
.social{margin-top:14px;font-size:7.5px;color:var(--navy);line-height:2}
.social span{display:inline-block;width:9px;height:9px;background:var(--blue);border-radius:2px;vertical-align:middle;margin-right:6px}
.cover{padding:0;background:linear-gradient(160deg,#1c4f94 0%,#0b2f6b 55%,#08204a 100%);color:var(--white)}
.cover .photo{position:absolute;inset:0}
.brand{position:relative;display:flex;align-items:center;gap:8px;padding:18px 20px;font-weight:800;font-size:15px;letter-spacing:1px;color:var(--white)}
.brand i{width:20px;height:20px;border-radius:50%;background:var(--white);display:block}
.cover-title{position:absolute;right:20px;top:288px;text-align:right;font-weight:800;font-size:19px;line-height:1.15;letter-spacing:.5px}
.cover-band{position:absolute;left:0;right:0;bottom:56px;height:118px;background:rgba(21,101,192,.88);text-align:right;padding:20px 20px;font-weight:700}
.cover-band .for{font-size:11px}
.cover-band .better{font-size:30px;font-weight:800;line-height:1.05}
.cover-band .healthier{font-size:17px}
.inside .panel{padding:0}
.inside .photo{height:128px}
.inside .body{padding:14px 18px}
ul{list-style:none;margin:4px 0 8px}
li{padding-left:9px;position:relative}
li::before{content:"";position:absolute;left:0;top:4px;width:4px;height:4px;background:var(--sky);border-radius:50%}
.label{font-weight:700;color:var(--navy);margin-top:4px}
</style>
</head>
<body>

<section class="spread outside">
  <div class="panel">
    <h2>What is whole body Cryotherapy?</h2>
    <p>Whole Body Cryotherapy is a process of cooling a person down to about 32 degrees Fahrenheit for up to 2-3 minutes.</p>
    <div class="stats">
      <div><svg width="30" height="30" viewBox="0 0 30 30"><circle cx="15" cy="15" r="12" fill="none" stroke="var(--blue)" stroke-width="2"/><path d="M15 8v7l5 3" stroke="var(--blue)" stroke-width="2" fill="none"/></svg>2-3 MINUTES</div>
      <div><svg width="30" height="30" viewBox="0 0 30 30"><rect x="12" y="3" width="6" height="18" rx="3" fill="none" stroke="var(--blue)" stroke-width="2"/><circle cx="15" cy="23" r="5" fill="var(--blue)"/></svg>-200°F TO -260°F</div>
    </div>
    <p>This is done by surrounding the body with an air temperature causing a natural fight-or-flight reaction. During this short exposure the body sends blood toward its core, protecting vital organs and warming the system.</p>
    <p>When the session ends the blood rushes back out to the limbs, carrying fresh oxygen and nutrients. This cycle helps the body release endorphins, ease tension and support natural repair from head to toe.</p>
    <p>This results in many beneficial effects, including pain relief, improved blood circulation, faster recovery after exercise, reduced swelling and a lift in mood, energy and overall sense of wellbeing.</p>
  </div>

  <div class="panel">
    <div class="seen-head">
      <div class="small">Where</div>
      <div class="big">WHOLE BODY CRYOTHERAPY<br>HAS BEEN SEEN ON?</div>
    </div>
    <div class="badges" role="img" aria-label="Media outlet badges">
      <div class="badge sq"></div><div class="badge"></div><div class="badge sq"></div><div class="badge"></div>
      <div class="badge"></div><div class="badge sq"></div><div class="badge"></div><div class="badge sq"></div>
      <div class="badge sq"></div><div class="badge"></div><div class="badge sq"></div><div class="badge"></div>
    </div>
    <div class="contact">218 LARCHMONT WAY<br>BROOKFIELD, PA 19350<br>PHONE 555-014-2290<br>EMAIL: HELLO@FERNVALECRYO.COM</div>
    <div class="social">
      <div><span></span>SOCIAL.PAGE/FERNVALECRYO</div>
      <div><span></span>@FERNVALECRYO</div>
      <div><span></span>@FERNVALE_CRYO</div>
    </div>
  </div>

  <div class="panel cover">
    <div class="photo" role="img" aria-label="Cryotherapy chamber in a cool blue treatment room" style="background:radial-gradient(circle at 60% 35%,rgba(160,205,240,.45),transparent 55%)"></div>
    <div class="brand"><i></i>FERNVALE CRYOTHERAPY</div>
    <div class="cover-title">WHOLE BODY<br>CRYOTHERAPY</div>
    <div class="cover-band">
      <div class="for">FOR A</div>
      <div class="better">BETTER</div>
      <div class="healthier">HEALTHIER YOU</div>
    </div>
  </div>
</section>

<section class="spread inside">
  <div class="panel">
    <div class="photo" role="img" aria-label="Person relaxing in a bright wellness setting" style="background:linear-gradient(135deg,#bcd9ef,#6fa6d3)"></div>
    <div class="body">
      <h2>Health and<br>Wellness</h2>
      <p>Whole Body Cryotherapy can help to ease and alleviate chronic health conditions such as fibromyalgia, rheumatoid arthritis, multiple sclerosis, lupus, immune deficiencies and more. It may help with anxiety and general fatigue. Cryotherapy is a natural, drug free approach that encourages the body to heal itself.</p>
      <p>Since the treatment takes only a few minutes it fits easily into a busy day, giving a calm reset for body and mind.</p>
      <div class="label">ADDITIONAL BENEFITS FOR HEALTH AND WELLNESS INCLUDE:</div>
      <ul>
        <li>Ease chronic pain and muscle tension</li>
        <li>Reduce inflammation and swelling</li>
        <li>Clearing of skin conditions</li>
        <li>Lift in mood and reduced stress</li>
        <li>Boost in energy and alertness</li>
        <li>Better quality of sleep</li>
        <li>Stronger immune response</li>
        <li>Improved blood circulation</li>
        <li>Better night's sleep</li>
      </ul>
    </div>
  </div>

  <div class="panel">
    <div class="photo" role="img" aria-label="Athlete in motion during training" style="background:linear-gradient(135deg,#2a6fb8,#0b2f6b)"></div>
    <div class="body">
      <h2>Recovery and<br>Performance</h2>
      <p>Professional teams and high performance athletes are now utilizing Whole Body Cryotherapy in their training plans. It helps speed recovery between sessions, lowers soreness after hard workouts and keeps the body ready for the next effort.</p>
      <p>Regular sessions reduce downtime from minor injuries and help athletes of every level train more often, recover faster and perform at their best on game day.</p>
      <div class="label">REPORTED BENEFITS OF WHOLE BODY CRYOTHERAPY FOR RECOVERY AND PERFORMANCE INCLUDE:</div>
      <ul>
        <li>Faster recovery time</li>
        <li>Reduced inflammation</li>
        <li>Increased range of motion and flexibility</li>
        <li>Increased endurance</li>
        <li>Less muscle soreness</li>
        <li>Tissue repair</li>
        <li>Increased energy levels</li>
      </ul>
    </div>
  </div>

  <div class="panel">
    <div class="photo" role="img" aria-label="Woman with clear glowing skin" style="background:linear-gradient(135deg,#e3eff8,#9cc3e3)"></div>
    <div class="body">
      <h2>Beauty and<br>Anti-Aging</h2>
      <div class="label">INCREASED METABOLISM AND WEIGHT LOSS</div>
      <p>By lowering your skin temperature the body works to warm itself back up, using stored energy. A single session can burn a notable number of calories as metabolism rises for hours afterward.</p>
      <div class="label">ANTI-AGING</div>
      <p>By boosting collagen production and circulation, sessions help skin look firmer, smoother and more even, reducing the look of fine lines, pores and puffiness.</p>
      <div class="label">ADDITIONAL BENEFITS:</div>
      <ul>
        <li>Tighter, firmer and more youthful skin</li>
        <li>Reduced look of cellulite</li>
        <li>Up to several hundred calories burned per session</li>
        <li>Improved tone and skin clarity</li>
        <li>Brighter complexion and fresh glow</li>
        <li>Healthier hair, nails and skin</li>
      </ul>
    </div>
  </div>
</section>

</body>
</html>
```